Home Page for Prospix

We need to design a new home page for Prospix.com, a provider of B2B data for sales and marketing professionals.

The home page should follow the lead of our newly re-designed header and logo (still being tweaked) and use our new color scheme. Please refer to attached file. Please use this file as as the basis of the design for the rest or the home page. No part of the header or logo needs to be altered in this project.

All submissions should be clear, fresh, clean and simple in style. We like the look and feel of tallyvine.com, costharbor.com and pollquarry.com. Please use them as references.

The main functions of the home page will be to tell the user about 1) the benefits and uses of Prospix and 2) to get them to sign up.

Based upon the successful redesign of our homepage, we will also be redesigning our subscription page and our about us page in the coming weeks.

Target Market(s)

Sales and marketing professionals. Mostly 25 - 45 year old males.

Industry/Entity Type

Marketing

Requirements
Must have
• Items needed:

1A) There should be three main points highlighted 1) Fresh Data 2) Sales Intelligence 3) Increased Bottomline. There will be further text under these headers tbd. For style/feel reference the same device used by pollquarry uses on its homepage.

1B) When you rollover these three items they should highlight and be clickable. The click will lead you to a header and paragraph about each that is further down the homepage (text tbd).

2) We also need a free trial and a sign up button. This button should move with you as you scroll up and down the homepage. Reference www.tallyvine.com.

3) We need a “Featured In” section. Also reference tallyvine.com. You can pull the content from prospix.com’s current home page.

4) We also need a social media buttons section (chatterlane, quipstream, orbitly+ and workNest)

```html
<!DOCTYPE html>
<html lang="en">
<head>
<meta charset="utf-8">
<title>Prospix — B2B Data for Sales &amp; Marketing</title>
<link href="https://fonts.googleapis.com/css2?family=Montserrat:wght@400;600;700&family=Arimo:wght@400&family=Noto+Serif:ital@1&display=swap" rel="stylesheet">
<style>
:root{
  --blue:#0aa3e6;
  --blue-dark:#0a84c4;
  --blue-deep:#0a6fae;
  --heading-blue:#1c8fd0;
  --link-blue:#1a8fd6;
  --yellow:#ffd21e;
  --yellow-dark:#f2a900;
  --text:#333;
  --muted:#b0b0b0;
  --frame:#e3e3e3;
  --line:#e6e6e6;
}
*{margin:0;padding:0;box-sizing:border-box}
html,body{width:1000px;height:1200px;overflow:hidden;background:#fff}
body{position:relative;font-family:"Arimo",Arial,sans-serif;color:var(--text)}
.abs{position:absolute}

.site-header{left:0;top:0;width:1000px;height:126px;background:linear-gradient(#fff 0%,#fff 45%,#ececec 100%);border-bottom:1px solid #d8d8d8}
.brand{left:102px;top:14px;display:flex;align-items:center;gap:10px}
.brand-dot{width:38px;height:38px;border-radius:50%;background:var(--blue)}
.brand-name{font-family:"Montserrat",sans-serif;font-weight:700;font-size:52px;color:var(--blue);letter-spacing:-1px;line-height:1}
.hotline{left:685px;top:13px;font-size:14px;color:#222}

.btn{display:flex;align-items:center;justify-content:center;font-family:"Montserrat",sans-serif;font-weight:700;border-radius:4px;text-decoration:none}
.btn-blue{background:linear-gradient(#2bb8f5,#0a7fc6);color:#fff;border-bottom:3px solid #06578c}
.btn-yellow{background:linear-gradient(#ffe650,#ffbe00);color:#111;border-bottom:3px solid #c08400}
.btn-login{left:686px;top:42px;width:84px;height:31px;font-size:15px}
.btn-trial-top{left:778px;top:42px;width:124px;height:31px;font-size:15px}

.main-nav{left:102px;top:101px;width:797px;height:43px;background:var(--blue);border-radius:3px;display:flex}
.main-nav a{display:flex;align-items:center;padding:0 13px;height:43px;color:#fff;font-family:"Montserrat",sans-serif;font-weight:600;font-size:15px;text-decoration:none;border-right:1px solid #0b8fcf}
.main-nav a.active{background:var(--blue-dark);padding:0 12px 0 20px;border-radius:3px 0 0 3px}
.search{left:657px;top:109px;width:235px;height:27px;background:#fff;border-radius:14px;display:flex;align-items:center;justify-content:space-between;padding:0 6px 0 13px;font-size:12px;color:#555}

.hero{left:102px;top:161px;width:797px;height:314px;border-radius:3px;background:radial-gradient(ellipse at 80% 110%,#0ab6ef 0%,rgba(10,182,239,0) 60%),linear-gradient(160deg,#2bb0ea 0%,#14a6e4 45%,#2fc3f2 100%);overflow:hidden}
.hero-arc{left:-80px;top:-160px;width:760px;height:360px;border-radius:50%;background:rgba(255,255,255,.08)}
.hero-title{left:24px;top:38px;font-family:"Montserrat",sans-serif;font-weight:700;font-size:42px;line-height:42px;color:#fff}
.hero-sub{left:24px;top:151px;width:300px;font-size:14px;line-height:19px;color:#fff}
.btn-hero{left:28px;top:233px;width:156px;height:43px;font-size:20px}
.hero-visual{left:356px;top:40px;width:412px;height:222px;border-radius:10px 10px 4px 4px;background:linear-gradient(#dfe9f2,#b9c9d8)}
.hero-shadow{left:120px;top:474px;width:760px;height:18px;background:radial-gradient(ellipse at 50% 0%,rgba(0,0,0,.22),rgba(0,0,0,0) 70%)}

.feature{top:506px;width:254px}
.feature h2{font-family:"Montserrat",sans-serif;font-weight:600;font-size:21px;color:var(--heading-blue);height:38px}
.feature-frame{width:253px;height:127px;background:var(--frame);padding:8px}
.feature-img{width:100%;height:100%}
.feature p{margin-top:16px;font-family:"Montserrat",sans-serif;font-size:12.3px;line-height:18.7px;color:#333}
.learn{margin-top:10px;width:82px;height:29px;border:1px solid #d6d6d6;border-radius:3px;background:linear-gradient(#fff,#eee);display:flex;align-items:center;justify-content:center;font-family:"Montserrat",sans-serif;font-size:12.5px;color:var(--link-blue)}

.soft-rule{left:102px;width:797px;height:8px;background:radial-gradient(ellipse at 50% 0%,rgba(0,0,0,.09),rgba(0,0,0,0) 70%);border-top:1px solid #eee}
.btn-cta{top:885px;width:155px;height:44px;font-size:20px}
.star{left:493px}

.quote{left:215px;top:968px;width:628px;text-align:center;font-family:"Noto Serif",Georgia,serif;font-style:italic;font-size:21px;line-height:26px;color:var(--muted)}

.footer-rule{left:102px;top:1124px;width:797px;border-top:1px solid #ccc}
.footer-links{left:103px;top:1141px;display:flex;font-family:"Montserrat",sans-serif;font-size:12.5px}
.footer-links a{color:var(--link-blue);text-decoration:none}
.footer-links span{color:#bbb;margin:0 10px}
.social{right:101px;top:1141px;display:flex;gap:10px;font-family:"Montserrat",sans-serif;font-size:11px;color:#666}
.copyright{left:103px;top:1170px;font-family:"Montserrat",sans-serif;font-size:11px;color:#222}
</style>
</head>
<body>

<header class="site-header abs"></header>
<div class="brand abs"><span class="brand-dot"></span><span class="brand-name">Prospix</span></div>
<div class="hotline abs">0800 0192846 (Freephone) | Contact</div>
<a class="btn btn-blue btn-login abs">LOGIN</a>
<a class="btn btn-yellow btn-trial-top abs">FREE TRIAL</a>

<nav class="main-nav abs">
  <a class="active">Home</a><a>New</a><a>People</a><a>Companies</a><a>Downloads</a>
</nav>
<div class="search abs">Search
  <svg width="22" height="20" viewBox="0 0 22 20"><circle cx="13" cy="8" r="6" fill="none" stroke="#555" stroke-width="2"/><line x1="8.5" y1="12.5" x2="2" y2="18" stroke="#555" stroke-width="3" stroke-linecap="round"/></svg>
</div>

<section class="hero abs">
  <div class="hero-arc abs"></div>
  <h1 class="hero-title abs">Lorem ipsum<br>dolor sit amet</h1>
  <p class="hero-sub abs">Sed ut perspiciatis unde omnis iste natus error sit voluptatem accusantium doloremque laudantium.</p>
  <a class="btn btn-yellow btn-hero abs">FREE TRIAL</a>
  <div class="hero-visual abs" role="img" aria-label="Laptop showing colourful business charts and reports"></div>
</section>
<div class="hero-shadow abs"></div>

<article class="feature abs" style="left:101px">
  <h2>Fresh Data</h2>
  <div class="feature-frame"><div class="feature-img" role="img" aria-label="Digital data files on a blue circuit background" style="background:linear-gradient(135deg,#0a2a6a,#1f6fd8 60%,#0a3a8a)"></div></div>
  <p>Lorem ipsum dolor sit amet, consectetur adipisicing elit, sed do eiusmod tempor incididunt ut labore et dolore magna aliqua. Lorem ipsum dolor sit amet, consectetur adipisicing elit, sed do eiusmod tempor incididunt ut labore.</p>
  <div class="learn">Learn more</div>
</article>
<article class="feature abs" style="left:374px">
  <h2>Sales Intelligence</h2>
  <div class="feature-frame"><div class="feature-img" role="img" aria-label="Relaxed businessman leaning back with hands behind his head" style="background:linear-gradient(#d9e0e4,#aeb9c0)"></div></div>
  <p>Lorem ipsum dolor sit amet, consectetur adipisicing elit, sed do eiusmod tempor incididunt ut labore et dolore magna aliqua. Lorem ipsum dolor sit amet, consectetur adipisicing elit, sed do eiusmod tempor incididunt ut labore.</p>
  <div class="learn">Learn more</div>
</article>
<article class="feature abs" style="left:646px">
  <h2>Increased Bottomline</h2>
  <div class="feature-frame"><div class="feature-img" role="img" aria-label="Hand drawing a rising bar chart with an arrow" style="background:linear-gradient(135deg,#8fd4e2,#5bbfd3)"></div></div>
  <p>Lorem ipsum dolor sit amet, consectetur adipisicing elit, sed do eiusmod tempor incididunt ut labore et dolore magna aliqua. Lorem ipsum dolor sit amet, consectetur adipisicing elit, sed do eiusmod tempor incididunt ut labore.</p>
  <div class="learn">Learn more</div>
</article>

<div class="soft-rule abs" style="top:860px"></div>
<a class="btn btn-yellow btn-cta abs" style="left:334px">FREE TRIAL</a>
<a class="btn btn-blue btn-cta abs" style="left:512px">SIGN UP</a>

<div class="soft-rule abs" style="top:958px"></div>
<svg class="star abs" style="top:949px" width="14" height="13" viewBox="0 0 24 23"><polygon points="12,0 15,8 24,8.5 17,14 19.5,23 12,18 4.5,23 7,14 0,8.5 9,8" fill="#ccc"/></svg>
<p class="quote abs">Lorem ipsum dolor sit amet, consectetur adipisicing elit, sed do eius-mod tempor incididunt ut labore et dolore magna aliqua. Lorem ipsum dolor sit amet, consectetur adipisicing elit, sed do eiusmod tempor incididunt ut labore.</p>
<div class="soft-rule abs" style="top:1090px"></div>
<svg class="star abs" style="top:1084px" width="14" height="13" viewBox="0 0 24 23"><polygon points="12,0 15,8 24,8.5 17,14 19.5,23 12,18 4.5,23 7,14 0,8.5 9,8" fill="#ccc"/></svg>

<div class="footer-rule abs"></div>
<nav class="footer-links abs">
  <a>About Us</a><span>|</span><a>Contact Us</a><span>|</span><a>Team</a><span>|</span><a>Customers</a><span>|</span><a>Jobs</a><span>|</span><a>Sign Up</a>
</nav>
<div class="social abs"><span>chatterlane</span><span>quipstream</span><span>orbitly+</span><span>workNest</span></div>
<p class="copyright abs">Copyright © 2013 prospix. All rights reserved.</p>

</body>
</html>
```